Business card for utility of the future

I need a business card template designed for brookvane. We provide sustainable water, energy and waste services to homes.

The card should include name, position, email address, phone number, website and our logo (attached). I would like it to convey professionalism and creativity.

Target Market(s)

Homeowners, investors, corporate partners.

Industry/Entity Type

Utility

Contact Information for Business Card

The card should include name, position, email address, phone number, website and our logo (attached).

```html
<!DOCTYPE html>
<html lang="en">
<head>
<meta charset="utf-8">
<title>brookvane — Business Card</title>
<link href="https://fonts.googleapis.com/css2?family=Montserrat:wght@400;600;700&display=swap" rel="stylesheet">
<style>
  :root {
    --backdrop: #3b2219;
    --card-light: #ffffff;
    --card-dark: #0e1113;
    --brand-green: #6cc07f;
    --ink: #1b1b1b;
    --ink-on-dark: #f2f2f2;
  }
  html, body {
    margin: 0;
    padding: 0;
    width: 1200px;
    height: 1000px;
    overflow: hidden;
    background: var(--backdrop);
  }
  .canvas {
    position: relative;
    width: 1200px;
    height: 1000px;
    font-family: "Montserrat", sans-serif;
  }
  .card {
    position: absolute;
    top: 202px;
    width: 336px;
    height: 589px;
    box-shadow: 3px 4px 8px rgba(0, 0, 0, 0.45);
  }
  .card--front {
    left: 226px;
    background: var(--card-light);
  }
  .card--back {
    left: 635px;
    background: var(--card-dark);
  }
  .contact {
    position: absolute;
    left: 26px;
    bottom: 22px;
    color: var(--ink);
  }
  .contact__name {
    margin: 0;
    font-size: 24px;
    font-weight: 700;
    line-height: 1;
    color: var(--brand-green);
    letter-spacing: 0.2px;
  }
  .contact__role {
    margin: 1px 0 9px;
    font-size: 20px;
    font-weight: 400;
    line-height: 1.1;
  }
  .contact__line {
    margin: 0;
    font-size: 16px;
    font-weight: 400;
    line-height: 19px;
  }
  .brand {
    position: absolute;
    top: 38px;
    right: 36px;
    margin: 0;
    font-size: 34px;
    font-weight: 600;
    line-height: 1;
    color: var(--ink-on-dark);
  }
</style>
</head>
<body>
  <div class="canvas">
    <section class="card card--front" aria-label="Business card front">
      <div class="contact">
        <p class="contact__name">JOHN DOE</p>
        <p class="contact__role">Manager</p>
        <p class="contact__line">+1 (888) 123- 1234</p>
        <p class="contact__line">www.yourwebsite.com</p>
        <p class="contact__line">youremail@domain.com</p>
      </div>
    </section>
    <section class="card card--back" aria-label="Business card back">
      <p class="brand">brookvane</p>
    </section>
  </div>
</body>
</html>
```